Design for company homepage promoting to the pharmaceutical industry

Our company produces medical education materials and services for the pharmaceutical industry. Our existing website (www.quorvan.net.au) provides more information.
 
We need a homepage design for our new company website we are creating. Our site will not have a great amount of content, we want it to be fast, user friendly and easily adaptable to viewing on any platform, and through any browser. We don't want it over-designed - i.e. no highly animated banner flags, backgrounds, obscure webfonts, too many graphics etc. Attached are files indicating our existing company logo and design. We want the logo and rings to be retained. We've also attached draft copy for the website.
The final website may be designed in Wordpress (still to be confirmed)
 
This is a design to replace the current site (www.quorvan.net.au). Content will also be revised.
Things we don't like about our current design - doesn't use our current branding, is not very exciting, old fashioned 'standard' format, too much content, just doesn't look that good, boring.
 
Examples of sites we like:
www.brelmot.com.au
http://factsheets.wondipaq.com.au/index.html
 
Features we like from these sites - fast, responsive, short and to the point, cross-platform compatible including smartphones, and looks good
 
Main reasons people will visit our site: to find out whether we can provide services they might be looking for, to make a decision on whether they are interested in what we offer so they can get in touch with us, and to get our contact details.
Main thing we want to achieve from website visits is that it looks good enough and provides enough summary information on us so that they want to get in touch with us, to offer us work or to ask us to come in and meet them to provide more info on what we do.
Two most important calls to action from our website
· make the decision that we can do what you are looking for
· get in touch with us.
Updates

Thanks everyone for your submissions. At this stage with the Christmas break upon us, we are yet to finalise our decision, and will make a decision early in the new year. I hope everyone has a good holiday break.
Kind regards
Doug

Target Market(s)

Pharmaceutical industry professionals, marketers and medical professionals.

Industry/Entity Type

Pharmaceutical

Requirements
Must have
• Company logo and rings must be incorporated, company colour - blue - must be in there.
Should not have
• Complex animation or graphics that will slow the upload or limit cross-platform compatability/viewing on smartphones etc.

```html
<!DOCTYPE html>
<html lang="en">
<head>
<meta charset="utf-8">
<title>Quorvan – Healthcare Communication Specialists</title>
<link href="https://fonts.googleapis.com/css2?family=Open+Sans:wght@400;600;700&family=Libre+Baskerville:wght@700&display=swap" rel="stylesheet">
<style>
:root{
  --brand-blue:#1d6fb5;
  --brand-deep:#0f4f8a;
  --sky:#4fa3e0;
  --nav-dark:#1b1f26;
  --ink:#222;
  --muted:#6a6a6a;
  --panel:#ececec;
  --white:#fff;
  --footer:#20252c;
  --alert:#c0392b;
  --footer-text:#d0d4d9;
}
*{box-sizing:border-box;margin:0;padding:0}
html,body{width:684px;height:1200px;overflow:hidden;background:var(--white)}
body{font-family:"Open Sans",Arial,sans-serif;color:var(--ink);position:relative}
.page{position:relative;width:684px;height:1200px}

.site-header{position:absolute;top:0;left:0;right:0;height:60px;background:var(--white)}
.brand{position:absolute;left:122px;top:12px;font-size:26px;font-weight:700;color:var(--brand-blue);display:flex;align-items:center;gap:6px}
.brand-dot{width:12px;height:12px;border-radius:50%;background:var(--brand-blue)}
.social{position:absolute;left:322px;top:14px;display:flex;gap:7px}
.social span{width:11px;height:11px;border-radius:50%;background:var(--brand-deep)}
.contact-top{position:absolute;right:54px;top:8px;font-size:11px;color:var(--ink);line-height:22px}
.contact-top div{display:flex;align-items:center;gap:6px}
.contact-top svg{width:16px;height:16px}

.main-nav{position:absolute;top:60px;left:0;right:0;height:26px;background:var(--nav-dark);display:flex;justify-content:flex-end;padding-right:70px}
.main-nav a{color:var(--white);text-decoration:none;font-size:11px;line-height:26px;padding:0 10px;font-weight:600}
.main-nav a.active{background:var(--brand-blue)}

.hero{position:absolute;top:86px;left:0;right:0;height:280px}
.hero-bg{position:absolute;inset:0;background:linear-gradient(180deg,#7cc4f2 0%,#2f86cf 55%,#1f5fa3 100%)}
.hero h1{position:absolute;top:56px;left:0;right:0;text-align:center;font-family:"Libre Baskerville",Georgia,serif;font-size:27px;line-height:34px;color:#111}
.hero p{position:absolute;top:132px;left:0;right:0;text-align:center;font-size:10px;color:var(--white);line-height:13px}
.hero-object{position:absolute;left:258px;top:165px;width:150px;height:70px;border-radius:40px;background:radial-gradient(ellipse at center,#3a4450 0%,rgba(58,68,80,0) 70%)}
.cta{position:absolute;left:290px;top:244px;width:104px;height:26px;background:#111;color:var(--white);font-size:11px;font-weight:700;text-align:center;line-height:26px;letter-spacing:.5px;text-decoration:none}

.services{position:absolute;top:366px;left:0;right:0;height:420px;background:var(--panel)}
.services h2{position:absolute;top:28px;left:0;right:0;text-align:center;color:var(--brand-blue);font-size:17px;font-weight:700}
.service{position:absolute;width:336px}
.service h3{color:var(--brand-deep);font-size:11px;font-weight:700;margin-bottom:3px}
.service p{font-size:8px;line-height:10px;color:var(--muted)}
.service-icon{position:absolute;width:72px;height:72px;border-radius:50%;border:3px solid var(--brand-deep);background:var(--white);display:flex;align-items:center;justify-content:center}
.service-icon svg{width:38px;height:38px}

.about{position:absolute;top:786px;left:0;right:0;height:196px;background:var(--brand-blue);color:var(--white)}
.about h2{position:absolute;left:142px;top:34px;width:236px;font-size:16px;font-weight:600;line-height:22px}
.about ul{position:absolute;left:150px;top:92px;width:224px;list-style:none;font-size:8px;line-height:10px}
.about li{margin-bottom:9px;padding-left:8px;position:relative}
.about li::before{content:"";position:absolute;left:0;top:3px;width:4px;height:4px;background:var(--white);border-radius:50%}
.about-photo{position:absolute;left:392px;top:40px;width:112px;height:114px;background:linear-gradient(135deg,#cfe8b8,#8ebf6a 60%,#5e8f3f);border:2px solid var(--white)}

.prelaunch{position:absolute;top:982px;left:0;right:0;height:158px;background:var(--white)}
.prelaunch h2{position:absolute;left:142px;top:26px;width:330px;font-size:14px;font-weight:600;color:var(--brand-blue);white-space:nowrap}
.prelaunch p{position:absolute;left:142px;top:54px;width:220px;font-size:8px;line-height:10px;color:var(--muted)}
.device{position:absolute;left:484px;top:24px;width:120px;height:84px;background:linear-gradient(180deg,#3a3f47,#1a1d22);border-radius:4px}

.site-footer{position:absolute;top:1140px;left:0;right:0;height:60px;background:var(--footer);color:var(--footer-text);font-size:8px}
.footer-col{position:absolute;top:14px;line-height:14px}
.footer-col div{display:flex;align-items:center;gap:5px}
.footer-col svg{width:9px;height:9px;flex:none}
.footer-address{width:150px}
.footer-address div{align-items:flex-start;line-height:11px}
.footer-address svg{margin-top:1px}
.footer-note{position:absolute;left:0;right:0;bottom:4px;text-align:center;font-size:6px;color:#8a9099}
</style>
</head>
<body>
<div class="page">
  <header class="site-header">
    <div class="brand"><span class="brand-dot"></span>Quorvan</div>
    <div class="social"><span></span><span></span><span></span></div>
    <div class="contact-top">
      <div><svg viewBox="0 0 16 16"><rect width="16" height="16" rx="3" fill="#c0392b"/><path d="M5 4l2 2-1 1.5c.6 1.3 1.3 2 2.5 2.5L10 9l2 2-1.3 1.3C7.5 12 4 8.5 3.7 5.3z" fill="#fff"/></svg>Tel 02 9140 3827</div>
      <div><svg viewBox="0 0 16 16"><rect width="16" height="16" rx="3" fill="#c0392b"/><rect x="4" y="6" width="8" height="6" fill="#fff"/><rect x="5.5" y="3.5" width="5" height="3" fill="#fff"/></svg>Fax 02 9140 3828</div>
    </div>
  </header>

  <nav class="main-nav">
    <a class="active" href="#">Who we are</a>
    <a href="#">What we do</a>
    <a href="#">Some of our work</a>
    <a href="#">Who we work with</a>
    <a href="#">Contact us</a>
  </nav>

  <section class="hero">
    <div class="hero-bg" role="img" aria-label="Blue medical background with a heartbeat line and anatomical figures"></div>
    <h1>we' re scientists, journalists<br>and marketers rolled into one.</h1>
    <p>At Quorvan we are healthcare communication specialists.<br>We create clear medical education for modern health teams.</p>
    <div class="hero-object" role="img" aria-label="Stethoscope resting on the banner"></div>
    <a class="cta" href="#">ENROLL NOW!</a>
  </section>

  <section class="services">
    <h2>HEALTHCARE COMMUNICATION SPECIALTS</h2>

    <div class="service-icon" style="left:132px;top:70px"><svg viewBox="0 0 40 40"><path d="M6 16h8l16-8v24l-16-8H6z" fill="#111"/><rect x="10" y="24" width="5" height="9" fill="#111"/></svg></div>
    <div class="service" style="left:222px;top:82px"><h3>PROMOTION</h3><p>Lorem ipsum dolor sit amet, consectetur adipiscing elit, sed diam nonummy nibh euismod tincidunt ut laoreet dolore magna aliquam erat volutpat.</p></div>

    <div class="service" style="left:132px;top:170px"><h3>EDUCATION</h3><p>Lorem ipsum dolor sit amet, consectetur adipiscing elit, sed diam nonummy nibh euismod tincidunt ut laoreet dolore magna aliquam erat volutpat.</p></div>
    <div class="service-icon" style="left:478px;top:158px"><svg viewBox="0 0 40 40"><path d="M4 14L20 5l16 9z" fill="#111"/><rect x="6" y="16" width="28" height="3" fill="#111"/><rect x="9" y="20" width="4" height="11" fill="#111"/><rect x="18" y="20" width="4" height="11" fill="#111"/><rect x="27" y="20" width="4" height="11" fill="#111"/><rect x="5" y="32" width="30" height="3" fill="#111"/></svg></div>

    <div class="service-icon" style="left:132px;top:244px"><svg viewBox="0 0 40 40"><circle cx="20" cy="20" r="15" fill="none" stroke="#111" stroke-width="3"/><ellipse cx="20" cy="20" rx="6" ry="15" fill="none" stroke="#111" stroke-width="2"/><path d="M5 20h30M8 12h24M8 28h24" stroke="#111" stroke-width="2"/></svg></div>
    <div class="service" style="left:222px;top:258px"><h3>PROGRAMS</h3><p>Lorem ipsum dolor sit amet, consectetur adipiscing elit, sed diam nonummy nibh euismod tincidunt ut laoreet dolore magna aliquam erat volutpat.</p></div>

    <div class="service" style="left:132px;top:346px"><h3>MEETINGS</h3><p>Lorem ipsum dolor sit amet, consectetur adipiscing elit, sed diam nonummy nibh euismod tincidunt ut laoreet dolore magna aliquam erat volutpat.</p></div>
    <div class="service-icon" style="left:478px;top:332px"><svg viewBox="0 0 40 40"><circle cx="20" cy="13" r="5" fill="#111"/><path d="M11 31c0-7 4-11 9-11s9 4 9 11z" fill="#111"/><circle cx="9" cy="17" r="4" fill="#111"/><path d="M2 31c0-6 3-9 7-9 2 0 3 .5 4 1.5-2 2-3 4.5-3 7.5z" fill="#111"/><circle cx="31" cy="17" r="4" fill="#111"/><path d="M38 31c0-6-3-9-7-9-2 0-3 .5-4 1.5 2 2 3 4.5 3 7.5z" fill="#111"/></svg></div>
  </section>

  <section class="about">
    <h2>At Quorvan we are healthcare<br>communication specialists</h2>
    <ul>
      <li>Strategic tools for brand promotion (such as detail aids, product monographs, case files and patient material)</li>
      <li>Complex programs such as clinical audits and product familiarisation programs</li>
      <li>Medical meetings and symposia</li>
    </ul>
    <div class="about-photo" role="img" aria-label="Photo of a woman holding a green apple outdoors"></div>
  </section>

  <section class="prelaunch">
    <h2>Looking for something different pre-launch?</h2>
    <p>Quorvan offers programs to help your team manage change in a fast moving market, built around clear evidence and real clinical needs. Our team brings strong writing, sound science and careful planning to every launch we support, from the first brief through to final review with your medical and marketing groups.</p>
    <div class="device" role="img" aria-label="Laptop showing a medical presentation"></div>
  </section>

  <footer class="site-footer">
    <div class="footer-col" style="left:142px">
      <div><svg viewBox="0 0 10 10"><rect x="1" y="2" width="8" height="6" fill="none" stroke="#d0d4d9"/><path d="M1 2l4 3 4-3" fill="none" stroke="#d0d4d9"/></svg>info@quorvan.net.au</div>
      <div><svg viewBox="0 0 10 10"><circle cx="5" cy="5" r="4" fill="none" stroke="#d0d4d9"/></svg>www.quorvan.net.au</div>
    </div>
    <div class="footer-col footer-address" style="left:296px">
      <div><svg viewBox="0 0 10 10"><path d="M5 1a3 3 0 013 3c0 2-3 5-3 5S2 6 2 4a3 3 0 013-3z" fill="#d0d4d9"/></svg><span>Level 4, 17 Marlow Street<br>Kelvale NSW 2199</span></div>
    </div>
    <div class="footer-col" style="left:484px">
      <div><svg viewBox="0 0 10 10"><path d="M2 1l2 2-1 1c.5 1 1 1.5 2 2l1-1 2 2-1 1C4 8 2 6 1 2z" fill="#d0d4d9"/></svg>Tel 02 9140 3827</div>
      <div><svg viewBox="0 0 10 10"><rect x="2" y="4" width="6" height="4" fill="#d0d4d9"/><rect x="3" y="1" width="4" height="3" fill="none" stroke="#d0d4d9"/></svg>Fax 02 9140 3828</div>
    </div>
    <div class="footer-note">© Quorvan. All rights reserved.</div>
  </footer>
</div>
</body>
</html>
```